Modern Homepage Design for brenvik.nl – Fish & Chicken Food Webshop

Brenvik.nl is an online store that sells fish and chicken food. The design should be visually appealing, easy to navigate, and optimized for e-commerce. We want a layout that helps customers quickly find what they need and encourages them to explore our products.
A good example of the style and structure we like is dierkamp.nl – clean layout, clear product focus, and user-friendly navigation.
Brand Colors (must be used):
Orange: #f7a441
Dark Gray: #3c3c3b
White: #ffffff
Please use these colors consistently throughout the design.
Homepage Requirements:
The homepage should include the following sections:
Main Slider / Hero Banner
A large, eye-catching slider at the top of the page to highlight promotions or featured categories.
Category Blocks
A section with clear, clickable blocks or tiles that link to main product categories (e.g., Fish Food, Chicken Food, Accessories).
Featured Products
A section showcasing selected or best-selling products.
Special Offers / Promotions
A space to highlight current deals or limited-time offers.
Three Banners in a Row
A section with three horizontal banners side by side, which can be used for promotions, shipping info, or other key messages.
Unique Selling Points (USPs)
A section that briefly explains what makes our store different (e.g., fast delivery, high-quality feed, trusted by professionals).
SEO Content Block
A short paragraph of text for SEO purposes (use Lorem Ipsum for dummy content).
Footer Design
Include space for contact information, navigation links, and social media.
Design Notes:
The design must be responsive and mobile-friendly.
Focus on clean layout, good spacing, and easy navigation.
Use modern fonts and a clear visual hierarchy.
We are only looking for the homepage design at this stage, but we may work with the selected designer on additional pages later.
Deliverables:
Homepage design in layered PSD, Figma, or Adobe XD format
Any fonts and assets used
Preview images/mockups
We look forward to seeing your ideas and working with a designer who can bring our brand to life with a fresh and functional homepage design.
Let us know if you have any questions.
Hobby Animal Keepers, Pet Owners
Animal Nutrition & Feed
2 page

```html
<!DOCTYPE html>
<html lang="en">
<head>
<meta charset="utf-8">
<title>Brenvik – Fish &amp; Chicken Feed Webshop</title>
<link href="https://fonts.googleapis.com/css2?family=Jost:wght@300;400;500;600&display=swap" rel="stylesheet">
<style>
:root{
  --orange:#f7a441;
  --dark:#3c3c3b;
  --white:#ffffff;
  --board:#878787;
  --slate:#1d262d;
  --muted:#8e8e8d;
  --input:#efefef;
}
*{box-sizing:border-box;margin:0;padding:0}
html,body{width:1200px;height:1200px;overflow:hidden}
body{background:var(--board);font-family:'Jost',sans-serif;color:var(--dark);position:relative}
.abs{position:absolute}
a{color:inherit}

/* ===== Desktop page ===== */
.desktop{left:112px;top:67px;width:443px;height:1068px;background:var(--white);overflow:hidden}
.site-header{left:0;top:0;width:443px;height:46px}
.burger{left:26px;top:14px;width:19px;height:17px}
.burger span{display:block;height:2px;background:var(--dark);margin-bottom:5.5px;border-radius:1px}
.brand{font-weight:600;color:var(--dark);letter-spacing:-0.3px;display:flex;align-items:center;gap:4px;white-space:nowrap}
.brand .dot{width:.7em;height:.7em;border-radius:50%;background:var(--orange);display:inline-block}
.desktop .brand{left:62px;top:8px;font-size:22px}
.btn-login{left:319px;top:13px;width:51px;height:17px;border-radius:9px;background:var(--white);box-shadow:0 1px 3px rgba(0,0,0,.35);font-size:8px;display:flex;align-items:center;justify-content:center}
.btn-sign{left:375px;top:13px;width:51px;height:17px;border-radius:9px;background:var(--dark);color:var(--white);font-size:8px;display:flex;align-items:center;justify-content:center}

.hero{left:0;top:46px;width:443px;height:165px;overflow:hidden}
.hero-photo{left:0;top:0;width:100%;height:100%;
  background:
   radial-gradient(ellipse 120px 90px at 330px 20px,#e79a3a 0%,#c07a2c 40%,transparent 75%),
   radial-gradient(ellipse 70px 60px at 400px 120px,#d8c38e 0%,#8b7a4e 50%,transparent 80%),
   linear-gradient(100deg,#1b2228 0%,#1f2a31 48%,#2b3a42 70%,#3f5b3a 100%)}
.hero-title{left:24px;top:34px;color:var(--white);font-size:19px;font-weight:500;letter-spacing:.3px;white-space:nowrap}
.search{top:77px;height:21px;font-size:7.5px;display:flex;align-items:center;white-space:nowrap}
.search.address{left:21px;width:140px;background:var(--input);border-radius:11px 0 0 11px;color:#7b7b7b;padding-left:10px;gap:8px}
.search.category{left:167px;width:63px;background:var(--input);padding:0 6px;justify-content:space-between;color:var(--dark)}
.search.go{left:235px;width:60px;background:var(--orange);border-radius:0 11px 11px 0;color:var(--white);justify-content:center}
.hero-links{left:29px;top:141px;display:flex;gap:16px;font-size:8px;color:var(--white)}
.hero-links a{text-decoration:underline}

.promo{top:236px;height:102px;border-radius:7px;overflow:hidden;background:var(--dark)}
.promo.percent{left:20px;width:159px}
.promo.percent .big{left:6px;top:22px;font-size:54px;font-weight:600;color:var(--orange);letter-spacing:-2px}
.promo.percent .ring{left:100px;top:20px;width:62px;height:62px;border-radius:50%;border:9px solid var(--white)}
.promo.tasty{left:192px;width:236px}
.tasty .real{left:12px;top:4px;font-size:30px;color:var(--orange);line-height:1}
.tasty .word{left:12px;top:32px;font-size:30px;color:var(--white);line-height:1}
.tasty .eat{left:15px;top:68px;font-size:10px;color:#f2c230;white-space:nowrap}
.tasty .badge{left:94px;top:55px;width:32px;height:32px;border-radius:50%;background:var(--orange);border:2px solid var(--white);display:flex;flex-direction:column;align-items:center;justify-content:center;font-size:11px;line-height:1;color:var(--dark)}
.tasty .badge small{font-size:2.5px}
.tasty .dish{left:148px;top:26px;width:92px;height:80px;border-radius:46px 46px 0 0;border:2px solid var(--white);background:radial-gradient(circle at 45% 55%,#e9d7a8,#c79454 45%,#6f7d3a 80%)}
.tasty .pan{left:114px;top:5px;width:40px;height:40px;border-radius:50%;background:radial-gradient(circle,#c8c8c8,#7a7a7a);border:3px solid var(--orange)}
.promo-dot{left:312px;top:222px;width:18px;height:18px;border-radius:50%;background:var(--orange)}
.promo-ring{left:424px;top:260px;width:21px;height:21px;border-radius:50%;border:2px solid var(--orange)}
.pager{left:294px;top:352px;display:flex;gap:3.5px;align-items:center}
.pager i{width:6px;height:6px;border-radius:50%;border:1px solid #777;display:block}
.pager i.on{background:#666}
.pager b{width:4px;height:5px;border-left:1px solid #777;border-right:1px solid #777;display:block;margin-left:3px}

.section-title{width:443px;left:0;text-align:center;font-size:15px;font-weight:400;letter-spacing:.3px}
.cat{top:435px;width:112px;height:197px;border:1px solid #9a9a9a;border-radius:8px;overflow:hidden;background:var(--white)}
.cat .band{left:0;top:0;width:100%;height:78px}
.cat .arch{left:14px;top:0;width:84px;height:92px;border-radius:0 0 42px 42px;text-align:center;padding-top:6px}
.cat .arch h3{font-size:17px;line-height:16px;font-weight:500;color:var(--white);letter-spacing:.3px}
.cat .arch p{font-size:4.6px;line-height:6px;margin:6px 6px 0;color:var(--white)}
.cat.fish .band,.cat.chicken .band{background:var(--dark)}
.cat.fish .arch,.cat.chicken .arch{background:var(--orange)}
.cat.acc .band{background:var(--orange)}
.cat.acc .arch{background:var(--dark)}
.cat .art{left:10px;top:92px;width:92px;height:72px;border-radius:30px}
.cat .cta{left:26px;top:172px;width:59px;height:17px;border-radius:9px;font-size:5.5px;display:flex;align-items:center;justify-content:center;color:var(--white);background:var(--dark)}
.cat.acc .cta{background:var(--orange)}

.product{width:131px;height:158px;border:1px solid #aaa;border-radius:6px;overflow:hidden;background:var(--white);text-align:center}
.product .photo{width:100%;height:104px}
.product h4{font-size:15px;font-weight:400;margin-top:7px;letter-spacing:.2px;white-space:nowrap}
.product h4 small{font-size:6px}
.product p{font-size:5.7px;line-height:7.5px;margin:4px 8px 0}

/* ===== Why choose us ===== */
.why{left:646px;top:66px;width:442px;height:210px;background:var(--dark);color:var(--white);text-align:center}
.why h2{font-size:15px;font-weight:400;margin-top:21px;letter-spacing:.3px}
.why .intro{font-size:7.3px;line-height:11.5px;width:360px;margin:6px auto 0}
.usp{top:91px;width:83px;height:86px;border:1px solid #777;border-radius:7px;padding-top:8px}
.usp svg{width:30px;height:34px;stroke:var(--white);fill:none;stroke-width:1.6;stroke-linecap:round;stroke-linejoin:round}
.usp h5{font-size:5.3px;font-weight:400;margin-top:7px}
.usp p{font-size:3.3px;line-height:4.5px;margin:2px 6px 0;color:#ddd}

/* ===== Footer ===== */
.footer{left:646px;top:288px;width:443px;height:194px;background:var(--dark);color:var(--muted)}
.footer .brand{left:23px;top:14px;font-size:21px;color:var(--muted)}
.footer .brand .dot{background:var(--muted)}
.footer .about{left:23px;top:47px;width:108px;font-size:6.8px;line-height:8.8px;font-weight:300}
.fcol{top:26px;font-size:7px;font-weight:300;line-height:11.8px;white-space:nowrap}
.fcol h6{font-size:7.5px;font-weight:400;margin-bottom:3px}
.social{left:46px;top:135px;display:flex;gap:11px}
.social i{width:7px;height:7px;border-radius:50%;border:1px solid var(--muted);display:block}
.footer .rule{left:23px;top:154px;width:403px;height:1px;background:#5a5a59}
.footer .copy{left:0;top:163px;width:443px;text-align:center;font-size:6.8px;font-weight:300}

/* ===== Mobile ===== */
.mobile{left:700px;top:570px;width:316px;height:565px;border-radius:37px;overflow:hidden;background:var(--slate)}
.m-header{left:0;top:0;width:316px;height:71px;background:var(--white)}
.mobile .burger{left:20px;top:32px;width:18px}
.mobile .burger span{margin-bottom:5px}
.mobile .brand{left:53px;top:26px;font-size:20px}
.m-user{left:194px;top:24px;width:30px;height:30px;border-radius:50%;background:var(--dark)}
.m-sign{left:232px;top:25px;width:69px;height:29px;border-radius:15px;background:var(--dark);color:var(--white);font-size:14px;display:flex;align-items:center;justify-content:center}
.m-hero{left:0;top:71px;width:316px;height:494px;
  background:
   radial-gradient(ellipse 150px 110px at 190px 60px,#c8823a 0%,#8e5224 45%,transparent 80%),
   radial-gradient(ellipse 120px 70px at 90px 160px,#e7a13e 0%,#b36f24 40%,transparent 75%),
   radial-gradient(ellipse 60px 80px at 310px 330px,#e39a34 0%,transparent 70%),
   linear-gradient(160deg,#2f3e2c 0%,#1e2a31 40%,#1a232a 100%)}
.m-title{left:0;top:196px;width:316px;text-align:center;color:var(--white);font-size:21px;font-weight:500;letter-spacing:.4px;white-space:nowrap}
.m-field{left:20px;width:272px;height:41px;background:var(--input);display:flex;align-items:center;font-size:15px}
.m-field.addr{top:245px;color:#9a9a9a;padding-left:14px;gap:24px;font-weight:300}
.m-field.cat{top:304px;padding:0 16px;justify-content:space-between;color:var(--dark)}
.m-go{left:20px;top:364px;width:272px;height:41px;border-radius:21px;background:var(--orange);color:var(--white);font-size:15px;display:flex;align-items:center;justify-content:center}
.m-links{left:0;top:467px;width:316px;display:flex;justify-content:center;gap:17px;color:var(--white);font-size:9px}
.m-links a{text-decoration:underline}
</style>
</head>
<body>

<!-- Desktop homepage -->
<main class="desktop abs">
  <header class="site-header abs">
    <div class="burger abs"><span></span><span></span><span></span></div>
    <div class="brand abs"><span class="dot"></span>Brenvik</div>
    <a class="btn-login abs">Login</a>
    <a class="btn-sign abs">Sign up</a>
  </header>

  <section class="hero abs">
    <div class="hero-photo abs" role="img" aria-label="Photo of fish and chicken feed pellets in a dark bowl on a slate board"></div>
    <h1 class="hero-title abs">Get your feed delivered</h1>
    <div class="search address abs">
      <svg width="7" height="9" viewBox="0 0 10 13"><path d="M5 0a5 5 0 0 0-5 5c0 3.6 5 8 5 8s5-4.4 5-8a5 5 0 0 0-5-5zm0 7a2 2 0 1 1 0-4 2 2 0 0 1 0 4z" fill="#3c3c3b"/></svg>
      Enter delivery Address
    </div>
    <div class="search category abs">Category <svg width="5" height="3" viewBox="0 0 6 3"><path d="M0 0h6L3 3z" fill="#3c3c3b"/></svg></div>
    <a class="search go abs">Get Feed</a>
    <nav class="hero-links abs"><a>Fish food</a><a>Chicken food</a><a>Accessories</a></nav>
  </section>

  <div class="promo percent abs">
    <span class="big abs">7%</span>
    <span class="ring abs"></span>
  </div>
  <div class="promo tasty abs">
    <span class="real abs">Real</span>
    <span class="word abs">Fresh</span>
    <span class="eat abs">FEED THEM WELL.</span>
    <span class="pan abs" role="img" aria-label="Photo of a scoop of fish food flakes"></span>
    <span class="dish abs" role="img" aria-label="Photo of a bag of chicken layer pellets"></span>
    <span class="badge abs">50%<small>BIG DISCOUNT</small></span>
  </div>
  <span class="promo-dot abs"></span>
  <span class="promo-ring abs"></span>
  <div class="pager abs"><i></i><i></i><i class="on"></i><i></i><i></i><i></i><i></i><b></b></div>

  <h2 class="section-title abs" style="top:390px">Explore our feed categories</h2>

  <article class="cat fish abs" style="left:21px">
    <div class="band abs"></div>
    <div class="arch abs"><h3>FISH<br>FOOD</h3><p>Flakes, pellets and sticks for pond and aquarium fish, rich in protein for healthy growth and bright colour.</p></div>
    <div class="art abs" role="img" aria-label="Illustration of koi fish with food pellets" style="background:radial-gradient(ellipse at 50% 55%,#c7782f,#e0a24a 55%,#fff 80%)"></div>
    <a class="cta abs">View Range</a>
  </article>
  <article class="cat chicken abs" style="left:172px">
    <div class="band abs"></div>
    <div class="arch abs"><h3>CHICKEN<br>FOOD</h3><p>Layer mash, grower crumbs and grain mixes that keep your flock strong, healthy and laying well all year.</p></div>
    <div class="art abs" role="img" aria-label="Illustration of a hen with a bowl of grain" style="background:radial-gradient(ellipse at 50% 55%,#e08a2a,#efaa52 55%,#fff 80%)"></div>
    <a class="cta abs">View Range</a>
  </article>
  <article class="cat acc abs" style="left:315px">
    <div class="band abs"></div>
    <div class="arch abs"><h3>ACCESS-<br>ORIES</h3><p>Feeders, drinkers, nets and pond care to complete your setup every day.</p></div>
    <div class="art abs" role="img" aria-label="Illustration of a poultry feeder, drinker and fish net" style="border-radius:8px;background:linear-gradient(90deg,#3f7d3a,#e8c15a 35%,#c9733a 60%,#e05a3a 85%,#fff)"></div>
    <a class="cta abs">Check It Out</a>
  </article>

  <h2 class="section-title abs" style="top:672px">Featured Products</h2>

  <article class="product abs" style="left:18px;top:715px">
    <div class="photo" role="img" aria-label="Photo of koi pellets in a keeper's hand" style="background:radial-gradient(ellipse at 50% 60%,#e9e3dc 0%,#d06a3a 35%,#8a5a3c 75%)"></div>
    <h4>Koi Special:</h4><p>Premium floating pellets for colour, growth and clear water.</p>
  </article>
  <article class="product abs" style="left:162px;top:715px">
    <div class="photo" role="img" aria-label="Photo of layer mash in a feed bowl" style="background:radial-gradient(ellipse at 55% 50%,#8a4a2c 0%,#c98a52 30%,#eeeae6 70%)"></div>
    <h4>Special <small>of the</small> Month</h4><p>Our featured layer mash of the month, at a sharp price for your flock.</p>
  </article>
  <article class="product abs" style="left:305px;top:715px">
    <div class="photo" role="img" aria-label="Photo of pond sticks beside a goldfish pond" style="background:radial-gradient(ellipse at 50% 60%,#6c5a44 0%,#a8844c 35%,#6f9a3a 55%,#e9ebe6 80%)"></div>
    <h4>Pond Sticks</h4><p>Easy-to-digest daily sticks for all pond fish in every season.</p>
  </article>
  <article class="product abs" style="left:18px;top:888px">
    <div class="photo" role="img" aria-label="Photo of grower crumbs with fresh greens" style="background:radial-gradient(ellipse at 50% 50%,#5a3a22 0%,#9a6a3a 35%,#6a8a3a 60%,#d9d4cc 85%)"></div>
    <h4>Grower Crumbs</h4><p>Balanced crumbs for young chicks, trusted by keepers.</p>
  </article>
  <article class="product abs" style="left:162px;top:888px">
    <div class="photo" role="img" aria-label="Photo of a colourful mixed grain feed in a bowl" style="background:radial-gradient(circle at 50% 50%,#e03a2a 0%,#f0b030 30%,#4a8a3a 55%,#2f5a5a 75%,#c9a27a 100%)"></div>
    <h4>Grain Delight</h4><p>A rich scratch mix of seeds and corn for a happy flock.</p>
  </article>
  <article class="product abs" style="left:305px;top:888px">
    <div class="photo" role="img" aria-label="Photo of dried mealworm treats in a dish" style="background:radial-gradient(ellipse at 50% 55%,#2a1a2a 0%,#9a2a3a 30%,#e4d4c8 60%,#f4f1ee 85%)"></div>
    <h4>Mealworm Treats</h4><p>A protein-rich snack for fish and hens, loved by every flock.</p>
  </article>
</main>

<!-- Why choose us -->
<section class="why abs">
  <h2>Why Choose Us?</h2>
  <p class="intro">Here at Brenvik, we’re all about fresh, healthy feed for your fish and chickens. Enjoy speedy delivery, top-quality nutrition, and the trust of happy keepers. See the difference!</p>
  <div class="usp abs" style="left:31px">
    <svg viewBox="0 0 30 34"><path d="M12 2c-2 2 2 3 0 5M17 2c-2 2 2 3 0 5"/><circle cx="15" cy="13" r="1.5"/><path d="M4 25a11 11 0 0 1 22 0zM2 28h26"/></svg>
    <h5>Fresh Feed Every Batch</h5><p>Feed stored cool and shipped fresh so every bag keeps its full nutrition.</p>
  </div>
  <div class="usp abs" style="left:131px">
    <svg viewBox="0 0 34 34"><circle cx="9" cy="25" r="3.5"/><circle cx="26" cy="25" r="3.5"/><path d="M12 25h10l3-9h4M22 25l-3-9h-8v5h-6M25 16l-2-5h-3M2 14h7M3 18h5"/></svg>
    <h5>Fast &amp; Reliable Delivery</h5><p>Get your feed delivered quickly and on time, wherever you are.</p>
  </div>
  <div class="usp abs" style="left:230px">
    <svg viewBox="0 0 30 34"><path d="M8 16a5 5 0 0 1 2-9 6 6 0 0 1 10 0 5 5 0 0 1 2 9v4H8z"/><path d="M8 20h14"/><path d="M7 30c2-5 14-5 16 0"/></svg>
    <h5>Expert-Approved Quality</h5><p>Every product is chosen by animal feed experts for top quality.</p>
  </div>
  <div class="usp abs" style="left:330px">
    <svg viewBox="0 0 34 34"><path d="M17 10s-5-3-5-6a2.5 2.5 0 0 1 5-1 2.5 2.5 0 0 1 5 1c0 3-5 6-5 6z" fill="#fff"/><circle cx="9" cy="17" r="3"/><circle cx="17" cy="16" r="3"/><circle cx="25" cy="17" r="3"/><path d="M3 28c0-5 12-5 12 0M11 27c0-6 12-6 12 0M19 28c0-5 12-5 12 0"/></svg>
    <h5>Trusted by Keepers</h5><p>Hundreds of hobby keepers come back for the feed their animals love.</p>
  </div>
</section>

<!-- Footer -->
<footer class="footer abs">
  <div class="brand abs"><span class="dot"></span>Brenvik</div>
  <p class="about abs">Our webshop offers fresh, high-quality feed with fast and reliable delivery. Trusted by hobby keepers and pet owners, we specialize in both fish and chicken food. Order online today and keep your animals healthy.</p>
  <div class="fcol abs" style="left:164px"><h6>About Brenvik</h6>About us<br>Contact<br>Accessories</div>
  <div class="fcol abs" style="left:260px"><h6>Quick Links</h6>Home<br>Fish Food<br>Chicken Food<br>Accessories</div>
  <div class="fcol abs" style="left:361px"><h6>Contact us</h6>+31 000 000 00<br>info@brenvik.nl<br>12 Veerstraat, Ede</div>
  <div class="social abs"><i></i><i></i><i></i></div>
  <div class="rule abs"></div>
  <p class="copy abs">© 2025 Brenvik. All Rights Reserved.</p>
</footer>

<!-- Mobile homepage -->
<main class="mobile abs">
  <header class="m-header abs">
    <div class="burger abs"><span></span><span></span><span></span></div>
    <div class="brand abs"><span class="dot"></span>Brenvik</div>
    <span class="m-user abs"><svg width="30" height="30" viewBox="0 0 30 30"><circle cx="15" cy="11" r="5" fill="#fff"/><path d="M6 24a9 8 0 0 1 18 0z" fill="#fff"/></svg></span>
    <a class="m-sign abs">Sign up</a>
  </header>
  <section class="m-hero abs" role="img" aria-label="Photo of fish and chicken feed pellets on a dark slate board"></section>
  <h1 class="m-title abs">Get your feed delivered</h1>
  <div class="m-field addr abs">
    <svg width="12" height="16" viewBox="0 0 10 13"><path d="M5 0a5 5 0 0 0-5 5c0 3.6 5 8 5 8s5-4.4 5-8a5 5 0 0 0-5-5zm0 7a2 2 0 1 1 0-4 2 2 0 0 1 0 4z" fill="#3c3c3b"/></svg>
    Enter delivery Address
  </div>
  <div class="m-field cat abs">Category <svg width="8" height="4" viewBox="0 0 6 3"><path d="M0 0h6L3 3z" fill="#3c3c3b"/></svg></div>
  <a class="m-go abs">Get Feed</a>
  <nav class="m-links abs"><a>Fish food</a><a>Chicken food</a><a>Accessories</a></nav>
</main>

</body>
</html>
```